Brazilian food stall looking for a make over

We need a new Design for the front of our stall that would look authentic, colourful and practical as we have to transport, set up and put down in few hours.
We are based in Brisbane and our business are call The Ember Stand.
We sell Brazilian traditional BBQ and vegetarians options at markets, festivals and privet functions. We are new to this business and at the moment we are using our own design as presented on the image below.
We would like to see designs that would be eye catching with high contrast for easy recognition of the product with a menu with images of the product.

Requirements
Must have
• A connection with the product that is Brazilian bbq

```html
<!DOCTYPE html>
<html lang="en">
<head>
<meta charset="utf-8">
<title>The Ember Stand – Stall Front Banners</title>
<link href="https://fonts.googleapis.com/css2?family=Courgette&family=Sniglet:wght@800&display=swap" rel="stylesheet">
<style>
  :root {
    --stage: #1a1a1a;
    --cream: #f7f4e2;
    --blue: #5a9bb8;
    --teal: #2e9c8a;
    --green: #1aa55f;
    --lime: #a9cc3e;
    --yellow: #e8cf3c;
    --sun: #f6bb3a;
    --orange: #f3a92f;
  }
  * { box-sizing: border-box; margin: 0; padding: 0; }
  html, body {
    width: 1200px; height: 1000px; overflow: hidden;
    background: var(--stage);
  }
  .canvas { position: relative; width: 1200px; height: 1000px; }
  .banner {
    position: absolute; left: 16px; width: 1168px; height: 272px;
    background: var(--cream); overflow: hidden;
  }
  .banner--tagline { top: 221px; }
  .banner--name { top: 506px; }
  .art { position: absolute; }
  .art--palms-left { left: 0; top: 6px; width: 262px; height: 266px;
    background: linear-gradient(135deg, var(--blue), var(--green) 55%, var(--yellow)); opacity: .85;
    border-radius: 40% 60% 0 0; }
  .art--palms-right { left: 905px; top: 6px; width: 263px; height: 266px;
    background: linear-gradient(225deg, var(--blue), var(--green) 55%, var(--yellow)); opacity: .85;
    border-radius: 60% 40% 0 0; }
  .art--sun-right { left: 1040px; top: 0; width: 128px; height: 120px;
    background: var(--sun); border-radius: 0 0 0 70%; }
  .art--sun-left { left: 0; top: 0; width: 130px; height: 120px;
    background: var(--sun); border-radius: 0 0 70% 0; }
  .art--skewer { left: 935px; top: 100px; width: 90px; height: 86px;
    background: linear-gradient(135deg, var(--lime), #c3d94a); border-radius: 40%; opacity: .8; }
  .art--coconut { left: 174px; top: 212px; width: 56px; height: 54px;
    background: var(--lime); border-radius: 50%; }
  .art--flourish-left { left: 0; top: 188px; width: 92px; height: 84px;
    background: linear-gradient(90deg, var(--green), var(--sun)); border-radius: 0 50% 0 0; opacity: .8; }
  .art--flourish-right { left: 1062px; top: 186px; width: 106px; height: 86px;
    background: linear-gradient(90deg, var(--lime), var(--orange)); border-radius: 50% 0 0 0; opacity: .8; }
  .tagline {
    position: absolute; left: 0; right: 0; top: 66px; text-align: center;
    font-family: "Courgette", cursive; font-size: 30px; color: var(--blue);
    white-space: nowrap;
  }
  .headline {
    position: absolute; left: 0; right: 0; top: 124px; text-align: center;
    font-family: "Sniglet", sans-serif; font-weight: 800; font-size: 58px; letter-spacing: 1px;
    line-height: 1; white-space: nowrap;
  }
  .headline span {
    background: linear-gradient(90deg, var(--blue), var(--green) 35%, var(--yellow) 58%, var(--blue) 66%, var(--yellow));
    -webkit-background-clip: text; background-clip: text; color: transparent;
  }
  .brand-name {
    position: absolute; left: 0; right: 0; top: 108px; text-align: center;
    font-family: "Sniglet", sans-serif; font-weight: 800; font-size: 56px; line-height: 70px;
    color: var(--green); letter-spacing: 1px; white-space: nowrap;
  }
</style>
</head>
<body>
<main class="canvas">
  <section class="banner banner--tagline">
    <div class="art art--palms-left" role="img" aria-label="Two palm trees in blue to green to yellow gradient"></div>
    <div class="art art--coconut" role="img" aria-label="Green coconut"></div>
    <div class="art art--flourish-left" role="img" aria-label="Green swirl flourish with small orange flower"></div>
    <div class="art art--sun-right" role="img" aria-label="Yellow sun in the corner"></div>
    <div class="art art--skewer" role="img" aria-label="Barbecue skewer with grilled pieces"></div>
    <div class="art art--flourish-right" role="img" aria-label="Orange floral ornament with small teal and lime flowers"></div>
    <p class="tagline">Delicious &amp; Tradicional</p>
    <h2 class="headline"><span>BRAZILIAN BBQ</span></h2>
  </section>

  <section class="banner banner--name">
    <div class="art art--sun-left" role="img" aria-label="Yellow sun in the corner"></div>
    <div class="art art--flourish-left" role="img" aria-label="Green swirl flourish with small orange flower"></div>
    <div class="art art--palms-right" role="img" aria-label="Two palm trees in yellow to green to blue gradient"></div>
    <div class="art art--flourish-right" role="img" aria-label="Orange floral ornament with small teal and lime flowers"></div>
    <h1 class="brand-name">The Ember Stand</h1>
  </section>
</main>
</body>
</html>
```